Board Presentation template

Design a simple and clean PowerPoint slide templates for a Board meeting. The slides should have predominantly white backgrounds and use the colors of our Logo (attached): Tones of grey and orange and blue.
The company name is called Harrowgate Loadline Works.
It sell, calibrate, service and repair industrial and commercial scales of all types. In particular, Truck scales, floor scales, counting scales and benchtop scales.
There is no website for Harrowgate Loadline Works, but we have three affiliates that have their own websites:
https://www.quillbeamweigh.com/
https://northvanetruckandbalancegroup.com/
https://kbtare.com/
Target Market(s)
Industrial and Commercial Weighing systems
Industry/Entity Type
Look and feel
Each slider illustrates characteristics of the customer's brand and the style your logo design should communicate.

```html
<!DOCTYPE html>
<html lang="en">
<head>
<meta charset="utf-8">
<title>Harrowgate Loadline Works – Board Presentation Template</title>
<link href="https://fonts.googleapis.com/css2?family=Oswald:wght@500;600&family=Roboto:wght@400;500;700&display=swap" rel="stylesheet">
<style>
:root{
  --slate:#37424b;
  --red:#c8202f;
  --blue:#2c4a7c;
  --text:#4a4f55;
  --canvas:#c9c9c9;
  --paper:#ffffff;
  --mist:#e4e7ec;
}
*{box-sizing:border-box;margin:0;padding:0}
html,body{width:1036px;height:1200px;overflow:hidden;background:var(--canvas)}
body{position:relative;font-family:'Roboto',Arial,sans-serif;color:var(--text)}
.slide{position:absolute;width:440px;height:247px;overflow:hidden;
  background:linear-gradient(180deg,var(--paper) 0%,#f4f5f7 55%,var(--mist) 100%);
  box-shadow:0 6px 18px rgba(0,0,0,.35)}
.col-l{left:70px}.col-r{left:526px}
.row1{top:83px}.row2{top:345px}.row3{top:607px}.row4{top:869px}

.heading{position:absolute;left:30px;top:22px;font-family:'Oswald',sans-serif;font-weight:500;
  font-size:20px;color:var(--slate);padding-left:10px;border-left:4px solid var(--red);line-height:24px}

/* company name: one colour, one weight, plain square beside */
.brand{position:absolute;display:flex;align-items:center;gap:4px;
  font-family:'Roboto',Arial,sans-serif;font-weight:500;color:var(--slate);line-height:1.15}
.brand::before{content:"";flex:none;width:6px;height:6px;background:var(--slate)}
.brand-corner{right:12px;top:16px;width:72px;font-size:6.5px}
.cover-brand{left:0;right:0;top:96px;justify-content:center;font-size:17px;gap:8px}
.cover-brand::before{width:12px;height:12px}
.divider-brand{left:0;right:0;top:44px;justify-content:center;font-size:10px;gap:6px}
.divider-brand::before{width:8px;height:8px}
.thanks-brand{left:54px;top:178px;font-size:10px;gap:6px}
.thanks-brand::before{width:8px;height:8px}

.footer{position:absolute;left:5px;right:5px;bottom:4px;height:16px;background:var(--slate);
  display:flex;align-items:center;gap:18px;padding-left:10px;color:#fff;font-size:5.2px}
.footer span{display:flex;align-items:center;gap:4px}
.footer svg{width:8px;height:8px}
.page{position:absolute;right:30px;bottom:26px;width:13px;height:13px;border:1.3px solid var(--slate);
  border-radius:50%;background:#fff;font-size:4.5px;color:var(--red);display:flex;align-items:center;justify-content:center;font-weight:700}
.page::after{content:"";position:absolute;left:50%;margin-left:-.65px;top:11px;width:1.3px;height:6px;background:var(--slate)}

/* title slide */
.cover-photo{position:absolute;inset:0;background:linear-gradient(180deg,#eef1f4 0%,#d6dbe1 45%,#9aa3ac 75%,#cfd4d9 100%)}
.cover-title{position:absolute;left:5px;right:5px;top:187px;height:38px;background:var(--slate);border-radius:6px;
  color:#fff;font-family:'Oswald',sans-serif;font-weight:500;font-size:23px;display:flex;align-items:center;justify-content:center}
.cover-date{position:absolute;left:14px;right:14px;top:228px;height:22px;background:var(--slate);border-radius:6px 6px 0 0;
  color:#fff;font-size:8.5px;text-align:center;padding-top:2px}
.cover-date::after{content:"";position:absolute;left:16px;right:16px;bottom:0;height:5px;background:#fff}

/* services */
.svc-line{position:absolute;left:0;top:0}
.svc{position:absolute;top:145px;width:120px;text-align:center}
.svc h3{font-size:10px;font-weight:700;color:var(--slate);margin-bottom:5px}
.svc p{font-size:7.2px;line-height:12.5px}

/* agenda */
.agenda{position:absolute;top:54px;width:170px}
.agenda li{list-style:none;border-bottom:1.2px solid var(--slate);position:relative;
  font-size:7.4px;font-weight:500;color:var(--slate);padding:4px 0 0 2px;height:22px;margin-bottom:9px}
.agenda li i{position:absolute;right:0;top:2px;width:11px;height:11px;border:1px solid var(--slate);border-radius:50%;
  font-style:normal;font-size:4.5px;color:var(--red);display:flex;align-items:center;justify-content:center;background:#fff}

.body-copy{position:absolute;font-size:6.9px;line-height:11.8px;text-align:justify}
.photo-ring{position:absolute;left:239px;top:33px;width:176px;height:176px;border-radius:50%;border:4px solid var(--slate);
  padding:5px;background:#fff}
.photo-ring div{width:100%;height:100%;border-radius:50%;background:radial-gradient(circle at 45% 40%,#b8c4d0,#5c6b7a 60%,#2d3a46)}

/* affiliates */
.aff{position:absolute;top:66px;width:128px;height:128px;border-radius:50%;border:3px solid var(--slate);padding:5px;background:#fff}
.aff div{width:100%;height:100%;border-radius:50%;display:flex;align-items:center;justify-content:center;text-align:center;
  font-family:'Oswald',sans-serif;font-weight:500;font-size:12px;line-height:1.2;padding:10px}
.aff .dark{background:var(--slate);color:#fff}
.aff .light{background:#fff;color:var(--slate)}

/* divider */
.divider-photo{position:absolute;left:0;right:0;bottom:0;height:120px;background:linear-gradient(180deg,rgba(255,255,255,0) 0%,#6f6a86 40%,#2e2640 100%)}
.divider-title{position:absolute;left:68px;top:86px;font-family:'Oswald',sans-serif;font-weight:600;font-size:35px;color:var(--slate);
  border-left:6px solid var(--red);padding-left:12px;line-height:40px;white-space:nowrap}

/* thank you */
.thanks-title{position:absolute;left:32px;top:20px;font-family:'Oswald',sans-serif;font-weight:600;font-size:39px;color:var(--slate);
  border-left:7px solid var(--red);padding-left:14px;line-height:46px}
.contact{position:absolute;left:54px;display:flex;align-items:center;gap:8px;font-size:9.5px;color:var(--slate)}
.contact b{width:17px;height:17px;border:1.3px solid var(--slate);border-radius:50%;display:flex;align-items:center;justify-content:center}
.contact svg{width:9px;height:9px}
.thanks-band{position:absolute;left:0;right:12px;bottom:4px;height:15px;background:linear-gradient(90deg,#222a31,#3d4852,#222a31)}
</style>
</head>
<body>

<svg width="0" height="0" style="position:absolute">
  <defs>
    <symbol id="phone" viewBox="0 0 24 24"><circle cx="12" cy="12" r="11" fill="none" stroke="currentColor" stroke-width="2"/><path d="M8 6l2.5 0 1 3-1.5 1.2a8 8 0 0 0 3.8 3.8L15 12.5l3 1v2.5c0 .8-.7 1.2-1.5 1.2C11 17 7 13 7 7.5 7 6.7 7.3 6 8 6z" fill="currentColor"/></symbol>
    <symbol id="mail" viewBox="0 0 24 24"><rect x="4" y="6.5" width="16" height="11" rx="1.5" fill="currentColor"/><path d="M4.5 7.5l7.5 6 7.5-6" fill="none" stroke="#fff" stroke-width="1.4"/></symbol>
  </defs>
</svg>

<!-- Title slide -->
<section class="slide col-l row1">
  <div class="cover-photo" role="img" aria-label="Boardroom with chairs around a long table and a city skyline through tall windows"></div>
  <div class="brand cover-brand">Harrowgate Loadline Works</div>
  <div class="cover-title">PRESENTATION TITLE</div>
  <div class="cover-date">OCTOBER 25,2025</div>
</section>

<!-- Services -->
<section class="slide col-r row1">
  <h2 class="heading">OUR SERVICES</h2>
  <div class="brand brand-corner">Harrowgate Loadline Works</div>
  <svg class="svc-line" width="440" height="247" viewBox="0 0 440 247">
    <g fill="none" stroke="#37424b" stroke-width="2">
      <path d="M72 108V130H360V108M216 108V130"/>
      <circle cx="72" cy="85" r="23" fill="#fff"/>
      <circle cx="216" cy="85" r="23" fill="#fff"/>
      <circle cx="360" cy="85" r="23" fill="#fff"/>
    </g>
    <g fill="#c8202f">
      <path d="M62 80l6-4 5 3 5-3 6 4-3 7-5 4-4-3-4 3-5-4z"/>
      <rect x="205" y="76" width="22" height="14" rx="2"/>
      <rect x="209" y="78" width="14" height="9" fill="#fff"/>
      <rect x="213" y="90" width="6" height="4"/><rect x="209" y="94" width="14" height="2"/>
      <path d="M351 85l6 6 12-12" fill="none" stroke="#c8202f" stroke-width="4" stroke-linecap="round" stroke-linejoin="round"/>
    </g>
  </svg>
  <div class="svc" style="left:21px"><h3>SERVICE 01</h3><p>Sed ut perspiciatis unde<br>omnis iste natus doloremque<br>laudantium, totam rem</p></div>
  <div class="svc" style="left:160px"><h3>SERVICE 02</h3><p>Sed ut perspiciatis unde<br>omnis iste natus doloremque<br>laudantium, totam rem</p></div>
  <div class="svc" style="left:299px"><h3>SERVICE 03</h3><p>Sed ut perspiciatis unde<br>omnis iste natus doloremque<br>laudantium, totam rem</p></div>
  <div class="page">05</div>
  <div class="footer"><span><svg><use href="#phone"/></svg>CALL US : +1 888 888 8888</span><span><svg><use href="#phone"/></svg>EMAIL : info@harrowgateloadline.com</span></div>
</section>

<!-- Agenda -->
<section class="slide col-l row2">
  <h2 class="heading">AGENDA</h2>
  <div class="brand brand-corner">Harrowgate Loadline Works</div>
  <ul class="agenda" style="left:30px">
    <li>Sed ut perspiciatis unde omnis iste natus<i>03</i></li>
    <li>Sed ut perspiciatis unde omnis iste natus<i>05</i></li>
    <li>Sed ut perspiciatis unde omnis iste natus<i>07</i></li>
    <li>Sed ut perspiciatis unde omnis iste natus<i>09</i></li>
    <li>Sed ut perspiciatis unde omnis iste natus<i>11</i></li>
  </ul>
  <ul class="agenda" style="left:232px">
    <li>Sed ut perspiciatis unde omnis iste natus<i>04</i></li>
    <li>Sed ut perspiciatis unde omnis iste natus<i>06</i></li>
    <li>Sed ut perspiciatis unde omnis iste natus<i>08</i></li>
    <li>Sed ut perspiciatis unde omnis iste natus<i>10</i></li>
    <li>Sed ut perspiciatis unde omnis iste natus<i>12</i></li>
  </ul>
  <div class="page">02</div>
  <div class="footer"><span><svg><use href="#phone"/></svg>CALL US : +1 888 888 8888</span><span><svg><use href="#phone"/></svg>EMAIL : info@harrowgateloadline.com</span></div>
</section>

<!-- Why choose us -->
<section class="slide col-r row2">
  <h2 class="heading">WHY CHOOSE US</h2>
  <p class="body-copy" style="left:41px;top:61px;width:171px">Sed ut perspiciatis unde omnis iste natus error sit voluptatem accusantium doloremque laudantium, totam rem aperiam, eaque ipsa quae ab illo inventore veritatis et quasi architecto beatae vitae dicta sunt explicabo. Nemo enim ipsam voluptatem quia voluptas sit aspernatur aut odit aut fugit, sed quia consequuntur magni dolores eos qui ratione voluptatem sequi nesciunt. Neque porro quisquam est, qui dolorem ipsum quia dolor sit amet, consectetur, adipisci velit, sed quia non numquam eius modi tempora incidunt ut labore et dolore magnam aliquam quaerat voluptatem</p>
  <div class="photo-ring"><div role="img" aria-label="Business team meeting in a bright modern office"></div></div>
  <div class="brand brand-corner">Harrowgate Loadline Works</div>
  <div class="page">06</div>
  <div class="footer"><span><svg><use href="#phone"/></svg>CALL US : +1 888 888 8888</span><span><svg><use href="#phone"/></svg>EMAIL : info@harrowgateloadline.com</span></div>
</section>

<!-- About -->
<section class="slide col-l row3">
  <h2 class="heading">ABOUT US</h2>
  <div class="brand brand-corner">Harrowgate Loadline Works</div>
  <p class="body-copy" style="left:30px;top:61px;width:170px">Sed ut perspiciatis unde omnis iste natus error sit voluptatem accusantium doloremque laudantium, totam rem aperiam, eaque ipsa quae ab illo inventore veritatis et quasi architecto beatae vitae dicta sunt explicabo. Nemo enim ipsam voluptatem quia voluptas sit aspernatur aut odit aut fugit, sed quia consequuntur magni dolores eos qui ratione voluptatem sequi nesciunt. Neque porro quisquam est, qui dolorem ipsum quia dolor sit amet, consectetur, adipisci velit, sed quia non numquam eius modi tempora incidunt ut labore et dolore magnam aliquam quaerat voluptatem</p>
  <p class="body-copy" style="left:227px;top:61px;width:170px">Sed ut perspiciatis unde omnis iste natus error sit voluptatem accusantium doloremque laudantium, totam rem aperiam, eaque ipsa quae ab illo inventore veritatis et quasi architecto beatae vitae dicta sunt explicabo. Nemo enim ipsam voluptatem quia voluptas sit aspernatur aut odit aut fugit, sed quia consequuntur magni dolores eos qui ratione voluptatem sequi nesciunt. Neque porro quisquam est, qui dolorem ipsum quia dolor sit amet, consectetur, adipisci velit, sed quia non numquam eius modi tempora incidunt ut labore et dolore magnam aliquam quaerat voluptatem</p>
  <div class="page">03</div>
  <div class="footer"><span><svg><use href="#phone"/></svg>CALL US : +1 888 888 8888</span><span><svg><use href="#phone"/></svg>EMAIL : info@harrowgateloadline.com</span></div>
</section>

<!-- Affiliates -->
<section class="slide col-r row3">
  <h2 class="heading">OUR AFFILIATES</h2>
  <div class="brand brand-corner">Harrowgate Loadline Works</div>
  <div class="aff" style="left:21px"><div class="dark">QUILLBEAM WEIGH</div></div>
  <div class="aff" style="left:156px"><div class="light">KB TARE</div></div>
  <div class="aff" style="left:291px"><div class="dark">NORTHVANE TRUCK &amp; BALANCE GROUP</div></div>
  <div class="page">07</div>
  <div class="footer"><span><svg><use href="#phone"/></svg>CALL US : +1 888 888 8888</span><span><svg><use href="#phone"/></svg>EMAIL : info@harrowgateloadline.com</span></div>
</section>

<!-- Section divider -->
<section class="slide col-l row4">
  <div class="divider-photo" role="img" aria-label="Silhouettes of business people working at a table over a city skyline"></div>
  <div class="brand divider-brand">Harrowgate Loadline Works</div>
  <h2 class="divider-title">SECTION DIVIDER TITLE</h2>
</section>

<!-- Thank you -->
<section class="slide col-r row4">
  <h2 class="thanks-title">THANK YOU</h2>
  <div class="contact" style="top:82px"><b><svg style="color:var(--red)"><use href="#phone"/></svg></b>CALL US : +1 888 888 8888</div>
  <div class="contact" style="top:108px"><b><svg style="color:var(--red)"><use href="#mail"/></svg></b>EMAIL : info@harrowgateloadline.com</div>
  <div class="brand thanks-brand">Harrowgate Loadline Works</div>
  <div class="thanks-band" role="img" aria-label="Dark strip of office photography"></div>
</section>

</body>
</html>
```